self serve frozen yogurt store

would like a postcard to use for promotional purposes. We are a self serve frozen business in Alder Ridge Shopping Center located in Wrenfield, Bayshore. We are opened 7 days a week. We offer 15 flavors and over 40 different toppings.

Store

```html
<!DOCTYPE html>
<html lang="en">
<head>
<meta charset="utf-8">
<title>Tangleberry Frozen Yogurt Postcard</title>
<link href="https://fonts.googleapis.com/css2?family=Fira+Sans+Condensed:wght@600;700;800;900&display=swap" rel="stylesheet">
<style>
  :root {
    --berry-red: #e2223f;
    --band-red: #d7203a;
    --grape: #8a2f8c;
    --white: #ffffff;
    --stripe-pink: #f58ab0;
    --stripe-yellow: #fbe97a;
  }
  * { margin: 0; padding: 0; box-sizing: border-box; }
  html, body { width: 1200px; height: 929px; overflow: hidden; background: #ffffff; }
  .postcard {
    position: relative;
    width: 1200px;
    height: 929px;
    overflow: hidden;
    font-family: "Fira Sans Condensed", "Arial Narrow", sans-serif;
    color: var(--white);
  }
  .backdrop {
    position: absolute;
    inset: 0 0 124px 0;
    background: linear-gradient(90deg, var(--stripe-pink) 0%, #f9b7b0 30%, var(--stripe-yellow) 50%, #f9b7b0 70%, var(--stripe-pink) 100%);
  }
  .badge {
    position: absolute;
    border-radius: 50%;
    display: flex;
    flex-direction: column;
    align-items: center;
    justify-content: center;
    text-align: center;
    line-height: 0.9;
    font-weight: 800;
  }
  .badge svg { position: absolute; inset: 0; width: 100%; height: 100%; }
  .badge span { position: relative; display: block; }
  .badge--main {
    left: 362px; top: 34px; width: 494px; height: 494px;
    background: var(--berry-red);
  }
  .badge--main .line-small { font-size: 72px; margin-bottom: 8px; }
  .badge--main .line-big { font-size: 118px; }
  .badge--toppings {
    left: 58px; top: 146px; width: 376px; height: 376px;
    background: var(--grape);
  }
  .badge--toppings .over { font-size: 58px; }
  .badge--toppings .count { font-size: 118px; }
  .badge--toppings .label { font-size: 48px; line-height: 1; }
  .badge--flavors {
    left: 840px; top: 186px; width: 330px; height: 330px;
    background: var(--grape);
  }
  .badge--flavors .count { font-size: 128px; }
  .badge--flavors .label { font-size: 60px; }
  .brand {
    position: absolute;
    left: 178px; top: 590px;
    display: flex;
    align-items: center;
    gap: 24px;
  }
  .brand-name {
    font-size: 134px;
    font-weight: 900;
    color: var(--grape);
    line-height: 1;
    letter-spacing: -1px;
  }
  .brand-dot {
    width: 100px; height: 100px;
    border-radius: 50%;
    background: var(--berry-red);
  }
  .brand-tagline {
    position: absolute;
    left: 312px; top: 738px;
    font-size: 58px;
    font-weight: 800;
    line-height: 1;
    color: var(--grape);
    letter-spacing: 1px;
  }
  .info-band {
    position: absolute;
    left: 0; right: 0; bottom: 0;
    height: 124px;
    background: var(--band-red);
    display: flex;
    align-items: center;
    justify-content: space-between;
    padding: 0 120px 0 64px;
    font-size: 38px;
    font-weight: 700;
  }
</style>
</head>
<body>
  <main class="postcard">
    <div class="backdrop" role="img" aria-label="Playful pattern of pink and yellow vertical stripes scattered with pastel dots"></div>

    <div class="badge badge--main">
      <svg viewBox="0 0 494 494" aria-hidden="true">
        <circle cx="247" cy="247" r="226" fill="none" stroke="var(--white)" stroke-width="9" stroke-linecap="round" stroke-dasharray="0.1 18"/>
      </svg>
      <span class="line-small">Self Serve</span>
      <span class="line-big">Frozen</span>
      <span class="line-big">Yogurt</span>
    </div>

    <div class="badge badge--toppings">
      <svg viewBox="0 0 376 376" aria-hidden="true">
        <circle cx="188" cy="188" r="170" fill="none" stroke="var(--white)" stroke-width="8" stroke-linecap="round" stroke-dasharray="0.1 15"/>
      </svg>
      <span class="over">Over</span>
      <span class="count">40</span>
      <span class="label">Different<br>Toppings</span>
    </div>

    <div class="badge badge--flavors">
      <svg viewBox="0 0 330 330" aria-hidden="true">
        <circle cx="165" cy="165" r="149" fill="none" stroke="var(--white)" stroke-width="8" stroke-linecap="round" stroke-dasharray="0.1 15"/>
      </svg>
      <span class="count">15</span>
      <span class="label">Flavors</span>
    </div>

    <div class="brand">
      <span class="brand-name">Tangleberry</span>
      <span class="brand-dot" aria-hidden="true"></span>
    </div>
    <div class="brand-tagline">FROZEN YOGURT</div>

    <footer class="info-band">
      <span class="address">Alder Ridge Shopping Center, Wrenfield, Bayshore.</span>
      <span class="hours">Open 7 Days.</span>
    </footer>
  </main>
</body>
</html>
```